Book Cover and Back Cover for Assemble Yourself™ Career Development Manual
Daniel R. Holbrook | Holbrook Advisory, LLC | danielrholbrook.example
Book Cover and Back Cover for Assemble Yourself™ Career Development Manual - Books
Creative Brief
BOOK COVER - blue (RGB 0.0.69) is background/foundational color - the title, "Assemble Yourself™", is orange (RGB 255.54.0), is centered - the subtitle, "A blueprint for utilizing the TRAV assessment to unlock your potential, develop your career, and advance your personal brand." is white, is centered - my name, "Daniel R. Holbrook", is at the bottom, is centered - graphic...I'd like to add a graphic at the bottom of the cover, please review my website, danielrholbrook.example, for ideas. I want it to marry the ideas of business strategy concepts, unlocking human potential, and career growth. BACK COVER - blue (RGB 0.0.69) is background/foundational color - at top center, in orange (RGB 255.54.0), "Inside this manual is the process that will unlock your potential", in a thinly outlined box - in the center is the text "Daniel R. Holbrook is a Licensed Conduct Pattern Examiner (LCPE), a Principal Expert in Staff Affairs (PESA) and a Kestrel Institute of World Commerce MBA graduate. He is owner of Holbrook Advisory, LLC, a coaching practice specializing in unlocking human potential and career advancement, is author of a book entitled Dreading Ordinariness, and is Assistant Director of the L. T. Brandt College of Commerce' Graduate Career Center where he provides career coaching to professional programs MBA students. Daniel is also Vice Chairman of the Phoenix Enterprise and Labor Growth council. Prior to his current roles, he spent more than a decade in recruitment, training and development, and operations management with organizations such as the Bright Harbor Inns and Retreats, VacaLink Worldwide, Meridel Care, and Silver Mesa College." - my picture, from http://danielrholbrook.example/about-2/, is incorporated into the above biography text - standard empty white box for ISBN barcode, at the bottom right - the "Holbrook Advisory" business logo, at bottom left
Books
Working professionals who are: - trying to discover their life's purpose - wanting a promotion at their current job - trying to transition to a different employer - looking for a step-by-step process
JPEG and PDF in 300dpi commercial printing use for 8x11 book cover with bleed

```html
<!DOCTYPE html>
<html lang="en">
<head>
<meta charset="utf-8">
<title>Assemble Yourself™ — Book Cover Spread</title>
<link href="https://fonts.googleapis.com/css2?family=Arimo:wght@400;700&display=swap" rel="stylesheet">
<style>
  :root {
    --page-bg: #ececec;
    --cover-blue: #000045;
    --spine-blue: #00003c;
    --accent-orange: #ff3600;
    --text-white: #ffffff;
    --text-soft: #dfe0ee;
    --photo-tone-a: #6f7f98;
    --photo-tone-b: #c9a58c;
    --art-light: #d9dae6;
    --art-mid: #8f91a8;
  }
  * { margin: 0; padding: 0; box-sizing: border-box; }
  html, body {
    width: 1200px; height: 847px; overflow: hidden;
    background: var(--page-bg);
    font-family: "Arimo", Arial, sans-serif;
  }
  .spread {
    position: absolute; left: 30px; top: 150px;
    width: 1140px; height: 548px;
    display: flex;
    box-shadow: 0 4px 14px rgba(0,0,0,0.25);
  }
  .back-cover, .front-cover {
    position: relative; background: var(--cover-blue); height: 100%;
  }
  .back-cover { width: 536px; }
  .spine { width: 38px; height: 100%; background: var(--spine-blue); position: relative; }
  .front-cover { width: 566px; }

  /* back cover */
  .teaser-box {
    position: absolute; left: 25px; top: 24px; width: 476px; height: 56px;
    border: 1px solid var(--accent-orange);
    color: var(--accent-orange);
    font-size: 14px; font-weight: 700; line-height: 1.35;
    display: flex; align-items: center; justify-content: center;
    text-align: center; padding: 0 40px;
  }
  .author-bio {
    position: absolute; left: 25px; top: 196px; width: 476px;
    color: var(--text-white); font-size: 9.3px; line-height: 1.72;
    font-weight: 700;
  }
  .author-photo {
    float: left; width: 100px; height: 112px; margin: 2px 10px 4px 0;
    background: linear-gradient(160deg, var(--photo-tone-a), var(--photo-tone-b));
  }
  .author-bio .name-lead { color: var(--accent-orange); }
  .barcode-box {
    position: absolute; left: 25px; top: 440px; width: 72px; height: 72px;
    background: var(--text-white);
  }
  .studio-mark {
    position: absolute; left: 222px; top: 472px;
    display: flex; align-items: center; gap: 7px;
    color: var(--text-white); font-size: 12px; font-weight: 700;
  }
  .studio-mark .dot { width: 18px; height: 18px; border-radius: 50%; background: var(--accent-orange); }

  /* spine */
  .spine-title {
    position: absolute; left: 50%; top: 70px;
    transform: translateX(-50%);
    writing-mode: vertical-rl;
    color: var(--accent-orange); font-size: 20px; font-weight: 400;
    letter-spacing: 0.5px; white-space: nowrap;
  }

  /* front cover */
  .book-title {
    position: absolute; left: 0; top: 38px; width: 100%;
    text-align: center;
    color: var(--accent-orange); font-size: 46px; font-weight: 400;
    line-height: 1.05; letter-spacing: -0.5px;
  }
  .book-title sup { font-size: 17px; vertical-align: top; position: relative; top: 4px; }
  .book-subtitle {
    position: absolute; left: 40px; top: 160px; width: 486px;
    text-align: center;
    color: var(--text-white); font-size: 11px; font-weight: 700; line-height: 1.5;
  }
  .cover-art {
    position: absolute; left: 178px; top: 212px; width: 210px; height: 268px;
    background: linear-gradient(180deg, var(--art-light), var(--art-mid) 55%, var(--accent-orange) 70%, var(--art-mid));
    opacity: 0.85;
  }
  .author-name {
    position: absolute; left: 0; top: 496px; width: 100%;
    text-align: center;
    color: var(--text-soft); font-size: 17px; font-weight: 700;
  }
</style>
</head>
<body>
  <div class="spread">
    <section class="back-cover">
      <div class="teaser-box">Inside this manual is the process that will unlock your potential</div>
      <div class="author-bio">
        <div class="author-photo" role="img" aria-label="Portrait photo of the author"></div>
        <span class="name-lead">DANIEL R. HOLBROOK</span> is a Licensed Conduct Pattern Examiner (LCPE), a Principal Expert in Staff Affairs (PESA) and a Kestrel Institute of World Commerce MBA graduate. He is owner of Holbrook Advisory, LLC, a coaching practice specializing in unlocking human potential and career advancement, is author of a book entitled Dreading Ordinariness, and is Assistant Director of the L. T. Brandt College of Commerce' Graduate Career Center where he provides career coaching to professional programs MBA students. Daniel is also Vice Chairman of the Phoenix Enterprise and Labor Growth council. Prior to his current roles, he spent more than a decade in recruitment, training and development, and operations management with organizations such as the Bright Harbor Inns and Retreats, VacaLink Worldwide, Meridel Care, and Silver Mesa College.
      </div>
      <div class="barcode-box"></div>
      <div class="studio-mark"><span class="dot"></span>Holbrook Advisory</div>
    </section>

    <div class="spine">
      <div class="spine-title">Assemble Yourself™</div>
    </div>

    <section class="front-cover">
      <h1 class="book-title">Assemble<br>Yourself<sup>™</sup></h1>
      <p class="book-subtitle">A blueprint for utilizing the TRAV assessment to unlock your potential, develop your career, and advance your personal brand</p>
      <div class="cover-art" role="img" aria-label="Illustration: light bulb formed from a word cloud of business and career growth terms"></div>
      <div class="author-name">Daniel R. Holbrook</div>
    </section>
  </div>
</body>
</html>
```